Magnetic Business card Design do a service provider

Hi,

The company aim is to provide all service needs under one roof. However, at the moment there is only Accounting, Electrical and IT branches. There will be more services coming onboard in the future.

I already have a logo designed (Company name is already part of the logo), I now need a magnetic business card designed.

The business card will contain the following:

- Company Logo
- Contact#
- E-mail
- enough space to add website URL (for future)
Updates

Project Deadline Extended Reason: HI All,The deadline has been extended due to not having enough time to review an overwhelming number of designs that has been submitted by lots of designers.I will be uploading a draft of designs that i have in mind.Thanks. Added Friday, January 22, 2016

Target Market(s)

Residential, Home-based Businesses, Small and Medium businesses

Industry/Entity Type

Business

Contact Information for Business Card

Contact#: 0491 738 552
E-mail: service@brightharborgroup.net.au

Font styles to use
Decorative
Script

Requirements
Must have
• Round edges
• Some form of logo incorporation as a background

```html
<!DOCTYPE html>
<html lang="en">
<head>
<meta charset="utf-8">
<title>Bright Harbor Group – Business Card</title>
<link rel="stylesheet" href="https://fonts.googleapis.com/css2?family=Open+Sans:wght@600&family=Handlee&display=swap">
<style>
  :root {
    --backdrop: #3a3a3c;
    --card-deep: #0a4d92;
    --card-mid: #0e5ca8;
    --card-light: #1668b8;
    --band: #2eb1e8;
    --ink-white: #ffffff;
  }
  * { margin: 0; padding: 0; box-sizing: border-box; }
  html, body {
    width: 1200px;
    height: 913px;
    overflow: hidden;
    background: var(--backdrop);
  }
  .stage {
    position: relative;
    width: 1200px;
    height: 913px;
  }
  .card {
    position: absolute;
    left: 170px;
    top: 196px;
    width: 860px;
    height: 520px;
    border-radius: 38px;
    background: linear-gradient(135deg, var(--card-light) 0%, var(--card-mid) 45%, var(--card-deep) 100%);
    box-shadow: 0 18px 40px rgba(0, 0, 0, 0.45);
    overflow: hidden;
  }
  .contact-band {
    position: absolute;
    left: 420px;
    right: 0;
    top: 150px;
    height: 104px;
    background: var(--band);
    padding: 16px 0 0 34px;
    color: var(--ink-white);
    font-family: "Handlee", cursive;
  }
  .contact-band .phone {
    font-size: 30px;
    letter-spacing: 2px;
    line-height: 36px;
    font-weight: 700;
  }
  .contact-band .email {
    font-size: 22px;
    line-height: 34px;
    letter-spacing: 0.5px;
  }
  .brand {
    position: absolute;
    left: 56px;
    top: 282px;
    display: flex;
    align-items: center;
    gap: 14px;
  }
  .brand-dot {
    width: 20px;
    height: 20px;
    border-radius: 50%;
    background: var(--ink-white);
  }
  .brand-name {
    font-family: "Open Sans", sans-serif;
    font-weight: 600;
    font-size: 34px;
    line-height: 44px;
    color: var(--ink-white);
    white-space: nowrap;
  }
</style>
</head>
<body>
  <main class="stage">
    <section class="card" aria-label="Bright Harbor Group business card">
      <div class="contact-band">
        <p class="phone">0491 738 552</p>
        <p class="email">service@brightharborgroup.net.au</p>
      </div>
      <div class="brand">
        <span class="brand-dot"></span>
        <span class="brand-name">Bright Harbor Group</span>
      </div>
    </section>
  </main>
</body>
</html>
```